Tactical Supply Company needing memorable business card design

Our tactical supply comapny is in need of a new business card design that will set us apart from the amateurs. We sell tactical gear ranging from backpacks and range bags to apparel and other gear. We are looking for a sharp design that incorporates our logo, website, and name. Our colors are white, red, and black, or any combination of the three, preferably red and black.
I have attached our logo with our name underneath but I have also edited that design with the logo incorporated next to the name (attached).

Target Market(s)

Law enforcement, military, tactical

Industry/Entity Type

Business

Contact Information for Business Card

Include www.fernhollowprovisions-demo.com

Colors
000000
ec1f27
ffffff

Requirements
Must have
• Our name, logo, and website. This is intended to be a memorable simple card, no name, address, email, or phone number info is necessary. Designs that do include this additional info will still be considered if they are absolutely spectacular.
Should not have
• A standard template design, I can create that in my own on Cardvellum. I am looking for a new, creative design that is completely unique to my company.

```html
<!DOCTYPE html>
<html lang="en">
<head>
<meta charset="utf-8">
<title>Fernhollow Provisions – Business Card</title>
<link href="https://fonts.googleapis.com/css2?family=Audiowide&display=swap" rel="stylesheet">
<style>
  :root {
    --black: #0b0b0b;
    --red: #ec1f27;
    --white: #ffffff;
    --backdrop: #d9d9d9;
  }
  * { margin: 0; padding: 0; box-sizing: border-box; }
  html, body { width: 1200px; height: 852px; overflow: hidden; }
  body {
    background: var(--backdrop);
    font-family: "Audiowide", sans-serif;
    position: relative;
  }
  .card {
    position: absolute;
    width: 520px;
    height: 300px;
    border-radius: 22px;
    overflow: hidden;
    background: var(--black);
  }
  .card svg { position: absolute; inset: 0; }
  .card-front { left: 90px; top: 120px; }
  .card-back { left: 590px; top: 430px; }
  .brand {
    position: absolute;
    display: flex;
    align-items: center;
    gap: 12px;
    color: var(--white);
    font-size: 24px;
    letter-spacing: 1px;
    white-space: nowrap;
  }
  .brand-mark {
    width: 22px;
    height: 22px;
    background: var(--red);
  }
  .card-front .brand { left: 70px; top: 128px; }
  .card-back .brand { left: 34px; top: 62px; }
  .holder-name {
    position: absolute;
    left: 34px;
    top: 208px;
    color: var(--white);
    font-size: 26px;
    letter-spacing: 1px;
  }
  .website {
    position: absolute;
    left: 34px;
    top: 248px;
    color: var(--white);
    font-size: 12px;
    letter-spacing: 1px;
    text-transform: uppercase;
  }
</style>
</head>
<body>
  <div class="card card-front">
    <svg width="520" height="300" viewBox="0 0 520 300">
      <polygon points="0,0 90,0 0,200" fill="var(--red)"/>
      <polygon points="300,300 520,300 520,170" fill="var(--red)"/>
    </svg>
    <div class="brand"><span class="brand-mark"></span>FERNHOLLOW PROVISIONS</div>
  </div>

  <div class="card card-back">
    <svg width="520" height="300" viewBox="0 0 520 300">
      <rect width="520" height="300" fill="var(--red)"/>
      <polygon points="0,0 250,0 500,40 420,270 0,160" fill="var(--black)"/>
      <polygon points="250,0 500,0 500,40" fill="var(--red)"/>
      <line x1="505" y1="30" x2="425" y2="280" stroke="var(--white)" stroke-width="4"/>
    </svg>
    <div class="brand"><span class="brand-mark"></span>FERNHOLLOW PROVISIONS</div>
    <div class="holder-name">YOUR NAME</div>
    <div class="website">www.fernhollowprovisions-demo.com</div>
  </div>
</body>
</html>
```